Ardenwell Building and Property Services needs a business card design

We need a business card design for our building and property services business. We already have a logo we just need a creative design and layout on a business card. Emphasis on clean, modern, professional.
Our client targets are mainly body corporates, building managers, construction managers.
We are a building services company that lean more to structural repair of buildings, through concrete rectification and carbon fibre strengthening.
We also refurbish facades, rendering, painting etc
We target higher end body corporates in prestigious locations, hence why we'd like our cards to reflect professionalism, strength, efficiency

Target Market(s)

body corporates, building managers, construction managers

Industry/Entity Type

Construction

Contact Information for Business Card

Ardenwell is the main word, with 'Building and Property Services' underneath.
Level 17, 82 Harlow Street
MERRIDALE
Melbourne
Vic 3094
T: 9518 2736
Duncan Ferris - Director
dunardenwell@mailbox-example.com

Requirements
Must have
• Stand out on the back of the card- strong/ bold, company logo
• All of the contact details written above
Should not have
• I'd like the card to stand out, especially on the back. Id like the company logo to be prominent, although feel free to be creative around it. But remain clean and professional

```html
<!DOCTYPE html>
<html lang="en">
<head>
<meta charset="utf-8">
<title>Ardenwell Building and Property Services – Business Card</title>
<link rel="stylesheet" href="https://fonts.googleapis.com/css2?family=Cinzel:wght@400;600&family=Tinos&display=swap">
<style>
  :root {
    --page-bg: #d9d6d2;
    --card-black: #050608;
    --card-black-edge: #15181d;
    --silver-light: #e4e4e4;
    --silver-mid: #b9b9b9;
    --silver-dark: #8d8d8d;
    --navy-ink: #14204a;
    --brand-blue: #2a7fc0;
    --deep-blue: #061a3a;
    --panel-blue: #0d3f78;
    --panel-glow: #1f6db5;
    --line-blue: #3aa3e6;
    --contact-text: #c9d3de;
  }
  * { box-sizing: border-box; margin: 0; padding: 0; }
  html, body { width: 1200px; height: 969px; overflow: hidden; }
  body {
    background: var(--page-bg);
    display: flex; align-items: center; justify-content: center;
  }
  .business-card {
    position: relative;
    width: 1000px; height: 569px;
    background: linear-gradient(180deg, var(--card-black) 0%, var(--card-black-edge) 54%);
    overflow: hidden;
    box-shadow: 0 14px 40px rgba(0,0,0,.35);
  }
  .brand {
    position: absolute; left: 0; right: 0; top: 150px;
    text-align: center;
    font-family: "Cinzel", serif;
    color: var(--brand-blue);
  }
  .brand-mark {
    display: inline-block; width: 18px; height: 18px;
    background: var(--brand-blue);
    margin-right: 16px; vertical-align: 6px;
  }
  .brand-name {
    font-size: 44px; font-weight: 400; letter-spacing: 5px;
  }
  .brand-tagline {
    margin-top: 4px;
    font-size: 11px; letter-spacing: 3px; text-transform: uppercase;
    color: var(--brand-blue);
  }
  .decor { position: absolute; left: 0; top: 0; }
  .name-band {
    position: absolute; left: 0; right: 0; top: 310px; height: 64px;
    display: flex; align-items: center; justify-content: center;
    font-family: "Cinzel", serif; font-weight: 600;
    color: var(--navy-ink);
  }
  .person-name { font-size: 38px; letter-spacing: 1px; }
  .person-role { font-size: 27px; margin-left: 10px; }
  .address, .contacts {
    position: absolute; top: 410px;
    font-family: "Tinos", serif;
    color: var(--contact-text);
    font-size: 26px; line-height: 38px;
  }
  .address { left: 55px; }
  .contacts { right: 45px; text-align: right; }
  .contact-line { display: flex; align-items: center; justify-content: flex-end; gap: 14px; }
  .contact-line.email { font-size: 22px; }
  .contact-icon { width: 24px; height: 24px; flex: none; }
</style>
</head>
<body>
<div class="business-card">
  <svg class="decor" width="1000" height="569" viewBox="0 0 1000 569" aria-hidden="true">
    <defs>
      <linearGradient id="silver" x1="0" y1="0" x2="0" y2="1">
        <stop offset="0" stop-color="var(--silver-dark)"/>
        <stop offset=".35" stop-color="var(--silver-light)"/>
        <stop offset="1" stop-color="var(--silver-mid)"/>
      </linearGradient>
      <radialGradient id="panel" cx=".55" cy=".3" r=".8">
        <stop offset="0" stop-color="var(--panel-glow)"/>
        <stop offset=".55" stop-color="var(--panel-blue)"/>
        <stop offset="1" stop-color="var(--deep-blue)"/>
      </radialGradient>
    </defs>
    <rect x="0" y="370" width="1000" height="199" fill="url(#panel)"/>
    <line x1="0" y1="376" x2="1000" y2="376" stroke="var(--line-blue)" stroke-width="1.5" opacity=".7"/>
    <path d="M0 306 H1000 V374 H560 L517 418 L474 374 H0 Z" fill="url(#silver)"/>
    <line x1="0" y1="306" x2="1000" y2="306" stroke="#f5f5f5" stroke-width="2"/>
    <line x1="507" y1="420" x2="507" y2="569" stroke="var(--line-blue)" stroke-width="2"/>
    <line x1="527" y1="420" x2="527" y2="569" stroke="var(--line-blue)" stroke-width="2"/>
    <path d="M474 382 L517 426 L560 382" fill="none" stroke="var(--line-blue)" stroke-width="2"/>
  </svg>

  <div class="brand">
    <div><span class="brand-mark"></span><span class="brand-name">ARDENWELL</span></div>
    <div class="brand-tagline">Building and Property Services</div>
  </div>

  <div class="name-band">
    <span class="person-name">Duncan Ferris</span>
    <span class="person-role">– Director</span>
  </div>

  <address class="address" style="font-style:normal">
    Level 17, 82 Harlow Street<br>
    MERRIDALE, Melbourne<br>
    Vic 3094
  </address>

  <div class="contacts">
    <div class="contact-line">9518 2736
      <svg class="contact-icon" viewBox="0 0 24 24" aria-hidden="true"><path d="M6.5 3 L9.5 3 L10.5 8 L8.3 9.5 C9.3 12 11.5 14.3 14.3 15.5 L15.8 13.4 L21 14.4 L21 17.5 C21 19 19.8 20.5 18 20.3 C10.5 19.5 4.2 13.3 3.6 6 C3.5 4.3 4.8 3 6.5 3 Z" fill="var(--contact-text)"/></svg>
    </div>
    <div class="contact-line email">dunardenwell@mailbox-example.com
      <svg class="contact-icon" viewBox="0 0 24 24" aria-hidden="true"><rect x="3" y="6" width="18" height="12" fill="var(--contact-text)"/><path d="M3 6 L12 13 L21 6" fill="none" stroke="var(--panel-blue)" stroke-width="1.6"/></svg>
    </div>
    <div class="contact-line">www.ardenwell-example.com
      <svg class="contact-icon" viewBox="0 0 24 24" aria-hidden="true"><circle cx="12" cy="12" r="9" fill="var(--contact-text)"/><path d="M3 12 H21 M12 3 C8 7 8 17 12 21 M12 3 C16 7 16 17 12 21" fill="none" stroke="var(--panel-blue)" stroke-width="1.4"/></svg>
    </div>
  </div>
</div>
</body>
</html>
```